Personal Card: Make it roar!

Hello to all designers,
Hope you're having a nice day/evening! Let's cut to the chase. I would like a modern, beautiful and professional personal business card; with a vector-art of a lion. I'd like the lion to be Blood Red. On a black background. I'm a Filipino, and would love to have my country's flag incorporated into the design. Id like the stars of my flag to be used in your designs if possible. The texts I want on the card are only my name, number, and email address. Colour of my name should be White, and my details Silver. The size and font should be simple and professional, you're in charge of that! The placements of the lion and my details will be yours to decide.

At the back of the card, I would like just the words "Thank You" (Silver) on a Black Background. Right on the center.

To summarise, my requirements are:
- Blood Red: Front Face of Lion, Vector-Art
- Black: Background
- Yellow: Three Stars used in the design
- White: Benedict Sr Talavera
- Silver: Number & Email (Where appropriate)
- Back of the card (Center). Silver: "Thank You"
- Please DON'T use the colour blue.

It's all about the Lion. Images you'll find attached are some images of Lions' faces which I particularly want to be captured and put onto the card. Convert it into a vector-art. A vector-art Lion. PLEASE use the images attached for inspiration only! Do not use it on your designs. Thank you very much for your time.

Good luck!

Ben
Updates

Hello Desginers, Please use Blood Red for the colour red in your designs:HEX: 8A0707RGB: 138,7,7Thank you,Ben Added Saturday, March 12, 2016

Target Market(s)

Potential Connections

Industry/Entity Type

It Professional

Contact Information for Business Card

Name: Benedict Sr Talavera
Email: bentalavera@mailhaven.co.uk
Number: 07382614927

Requirements
Must have
• Modern, Professional & Simple
• (Blood Red HEX: 8A0707, RGB: 138,7,7) Lion (Vector-style art)
• (Black) Background
• (White) My Name
• (Silver) My Details
• Back of card: "Thank You" in Silver. Font size should be small/medium.
• Only colours that should be used are Red, Black, Yellow and White/Silver
Nice to have
• - Use of 3 Yellow stars on the design
Should not have
• - Please avoid using any other colours apart from those specified.

```html
<!DOCTYPE html>
<html lang="en">
<head>
<meta charset="utf-8">
<title>Benedict Sr Talavera — Business Card</title>
<link rel="stylesheet" href="https://fonts.googleapis.com/css2?family=Noto+Serif:wght@400&family=Roboto:wght@400&display=swap">
<style>
  :root {
    --stage: #1e1e1f;
    --card: #232323;
    --card-edge: #8a0707;
    --blood-red: #8a0707;
    --lion-glow: #b30f0f;
    --star-yellow: #f2b705;
    --name-white: #ffffff;
    --silver: #d6d6d6;
    --label-red: #c0120f;
  }
  * { box-sizing: border-box; margin: 0; padding: 0; }
  html, body {
    width: 1200px;
    height: 960px;
    overflow: hidden;
    background: var(--stage);
  }
  .canvas {
    position: relative;
    width: 1200px;
    height: 960px;
    display: flex;
    justify-content: center;
    align-items: center;
    gap: 90px;
  }
  .card {
    position: relative;
    width: 370px;
    height: 572px;
    background: var(--card);
    border-right: 3px solid var(--card-edge);
    border-bottom: 3px solid var(--card-edge);
    box-shadow: 0 18px 40px rgba(0, 0, 0, 0.55);
  }
  .card--front .star {
    position: absolute;
    width: 18px;
    height: 18px;
    fill: var(--star-yellow);
  }
  .star--top-left { left: 58px; top: 48px; }
  .star--right { left: 300px; top: 132px; }
  .star--below { left: 176px; top: 270px; }
  .lion-art {
    position: absolute;
    left: 88px;
    top: 60px;
    width: 196px;
    height: 200px;
    border-radius: 48% 48% 46% 46%;
    background: radial-gradient(circle at 50% 45%, var(--lion-glow) 0%, var(--blood-red) 62%, #5c0505 100%);
  }
  .name {
    position: absolute;
    left: 0;
    right: 0;
    top: 304px;
    text-align: center;
    font-family: "Noto Serif", Georgia, serif;
    font-size: 36px;
    line-height: 1.22;
    color: var(--name-white);
  }
  .contact {
    position: absolute;
    left: 58px;
    top: 432px;
    font-family: "Roboto", Arial, sans-serif;
    font-size: 17px;
    line-height: 1.6;
    color: var(--silver);
    list-style: none;
  }
  .contact__label {
    display: inline-block;
    width: 20px;
    color: var(--label-red);
  }
  .card--back {
    display: flex;
    align-items: center;
    justify-content: center;
  }
  .thank-you {
    font-family: "Noto Serif", Georgia, serif;
    font-size: 46px;
    line-height: 1.12;
    text-align: center;
    color: var(--silver);
    letter-spacing: 1px;
  }
</style>
</head>
<body>
<main class="canvas">
  <section class="card card--front" aria-label="Front of business card">
    <svg class="star star--top-left" viewBox="0 0 24 24" aria-hidden="true"><polygon points="12,1 14.9,8.6 23,9 16.7,14.1 18.8,22 12,17.6 5.2,22 7.3,14.1 1,9 9.1,8.6"/></svg>
    <svg class="star star--right" viewBox="0 0 24 24" aria-hidden="true"><polygon points="12,1 14.9,8.6 23,9 16.7,14.1 18.8,22 12,17.6 5.2,22 7.3,14.1 1,9 9.1,8.6"/></svg>
    <svg class="star star--below" viewBox="0 0 24 24" aria-hidden="true"><polygon points="12,1 14.9,8.6 23,9 16.7,14.1 18.8,22 12,17.6 5.2,22 7.3,14.1 1,9 9.1,8.6"/></svg>
    <div class="lion-art" role="img" aria-label="Blood red vector illustration of a lion's head with a full mane"></div>
    <h1 class="name">Benedict<br>Sr Talavera</h1>
    <ul class="contact">
      <li><span class="contact__label">M</span>0738 261 4927</li>
      <li><span class="contact__label">E</span>bentalavera@mailhaven.co.uk</li>
    </ul>
  </section>
  <section class="card card--back" aria-label="Back of business card">
    <p class="thank-you">Thank<br>You</p>
  </section>
</main>
</body>
</html>
```